Simple elegant business card

General card for a fin and television director.
Just want name, email, phone and address.

Target Market(s)

Prospective employers

Industry/Entity Type

Business

Requirements
Must have
• As above
Nice to have
• Logo but not necessary.
Should not have
• Not too colourful or funky.
• Simplicity and elegance the way to go.

```html
<!DOCTYPE html>
<html lang="en">
<head>
<meta charset="utf-8">
<title>Nora Vale – Director Business Card</title>
<link href="https://fonts.googleapis.com/css2?family=Arimo:wght@400&family=Josefin+Sans:wght@300&display=swap" rel="stylesheet">
<style>
  :root {
    --page-bg: #e9e7e4;
    --card-edge: #050505;
    --card-glow: #3b3b3b;
    --name-white: #f4f4f4;
    --title-grey: #8a8a8a;
    --contact-grey: #d6d6d6;
  }
  html, body {
    margin: 0;
    padding: 0;
    width: 1200px;
    height: 1000px;
    overflow: hidden;
    background: var(--page-bg);
  }
  .business-card {
    position: absolute;
    left: 150px;
    top: 256px;
    width: 900px;
    height: 487px;
    background: radial-gradient(ellipse 48% 58% at 42% 40%, var(--card-glow) 0%, #1a1a1a 50%, var(--card-edge) 100%);
    box-shadow: 0 6px 22px rgba(0,0,0,0.25);
  }
  .name-block {
    position: absolute;
    left: 0;
    top: 198px;
    width: 900px;
    text-align: center;
  }
  .person-name {
    margin: 0;
    font-family: "Arimo", Arial, sans-serif;
    font-weight: 400;
    font-size: 54px;
    line-height: 58px;
    color: var(--name-white);
    letter-spacing: 0.5px;
  }
  .job-title {
    margin: -2px 0 0;
    font-family: "Arimo", Arial, sans-serif;
    font-size: 19px;
    line-height: 20px;
    letter-spacing: 10px;
    padding-left: 10px;
    color: var(--title-grey);
  }
  .contact-list {
    position: absolute;
    left: 0;
    top: 352px;
    width: 900px;
    margin: 0;
    padding: 0;
    list-style: none;
    text-align: center;
    font-family: "Josefin Sans", sans-serif;
    font-weight: 300;
    font-size: 16px;
    line-height: 26.5px;
    color: var(--contact-grey);
    letter-spacing: 0.3px;
  }
</style>
</head>
<body>
  <section class="business-card">
    <div class="name-block">
      <h1 class="person-name">Nora Vale</h1>
      <p class="job-title">DIRECTOR</p>
    </div>
    <ul class="contact-list">
      <li class="contact-phone">+1 310 555 0142</li>
      <li class="contact-address">P.O. Box 118 Elmstreet 4170 Qld</li>
      <li class="contact-email">noravale@mail.com</li>
    </ul>
  </section>
</body>
</html>
```